SIGN UP PAGE AND CHECK OUT PROCESS DESIGN NEEDED

I offer a subscription service. Two products that offer the same exact features just two different prices as the cheaper product offers limited of all the features....<br/><br/>PLEASE USE EXISTING THEME OF CURRENT DESIGN JUST MAKE AN IMPROVED SIGN UP PAGE. <br/><br/><br/>NEED SIGN UP PAGE for a subscription service..... <br/>This is my current sign up page, only offers one product: https://www.brightloomrewards.biz/?page=signup <br/><br/>Please use all the same fields and content listed on this sign up page also please do a fake sign up to see the credit card page. I also need the credit card page to be designed....or if you want to combine the sign up and credit card page, etc. all in one I am open for that too....my goal is a super quick an easy sign up for customer. <br/><br/> AL A CARTE PROGRAM<br/>1 CERTIFICATE TYPE EACH MONTH<br/>$49/MTH MONTH TO MONTH BASIS NO CONTRACTS<br/>$239 ONE TIME PAYMENT FOR 6 MTHS OF SERVICE<br/>$399 ONE TIME PAYMENT FOR 12 MONTHS OF SERVICE<br/><br/>FEATURES:<br/><br/>UNLIMITED CERTIFICATE PDF DOWNLOADS<br/><br/>UNLIMITED E-MAIL CERTIFICATES<br/><br/>UNLIMITED TEXT/SMS CERTIFICATES<br/><br/>UNLIMITED API USAGE<br/><br/>UNLIMITED WEB BANNER CERTIFICATES<br/><br/>FULL REDEMPTION TRACKING<br/><br/>CERTIFICATE DISTRIBUTION REPORTS<br/><br/>WHITE LABEL REDEMPTION SITE<br/><br/>END USER MARKETING VIDEOS<br/><br/>MARKETING POSTERS AND FLYERS<br/><br/>PRODUCT DESCRIPTIONI BROCHURES<br/><br/>THE LATEST TIPS<br/><br/>SEPERATE REDEMPTION WEBSITES<br/><br/>CONTACT US 24/7<br/><br/>AFFILIATE PROGRAM<br/><br/>DISCOUNT TRAVEL BOOKING ENGINE<br/><br/>UNLIMITED PROGRAM<br/>UNLIMITED AMOUNTS OF ALL THE CERTIFICATES<br/>$99/MTH MONTH TO MONTH BASIS NO CONTRACTS<br/>$495 ONE TIME PAYMENT FOR 6 MTHS OF SERVICE<br/>$2,295 ONE TIME PAYMENT FOR 12 MONTHS OF SERVICE<br/><br/>FEATURES:<br/><br/>UNLIMITED CERTIFICATE PDF DOWNLOADS<br/><br/>UNLIMITED E-MAIL CERTIFICATES<br/><br/>UNLIMITED TEXT/SMS CERTIFICATES<br/><br/>UNLIMITED API USAGE<br/><br/>UNLIMITED WEB BANNER CERTIFICATES<br/><br/>FULL REDEMPTION TRACKING<br/><br/>CERTIFICATE DISTRIBUTION REPORTS<br/><br/>WHITE LABEL REDEMPTION SITE<br/><br/>END USER MARKETING VIDEOS<br/><br/>MARKETING POSTERS AND FLYERS<br/><br/>PRODUCT DESCRIPTIONI BROCHURES<br/><br/>THE LATEST TIPS<br/><br/>SEPERATE REDEMPTION WEBSITES<br/><br/>CONTACT US 24/7<br/><br/>AFFILIATE PROGRAM<br/><br/>DISCOUNT TRAVEL BOOKING ENGINE<br/><br/><br/>

Target Market(s)

B2B SMALL BUSINESS OWNERS
MARKETERS
ADVERTISERS

Industry/Entity Type

Digital Marketing

Number of Pages Required

3 page

Colors

Designer to choose colors to be used in the design.

Requirements
Must have
• MUST MATCH EXISTING THEME
Nice to have
• A VERY MODERN DESIGN

```html
<!DOCTYPE html>
<html lang="en">
<head>
<meta charset="utf-8">
<title>Brightloom Rewards – Select Program</title>
<link rel="stylesheet" href="https://fonts.googleapis.com/css2?family=Roboto:wght@400;500;700&display=swap">
<style>
:root{
  --canvas:#d6d6d6;
  --header:#222325;
  --nav:#0a72c8;
  --brand:#3a90dc;
  --tab-on:#0a6cc4;
  --tab-off:#dcdcdc;
  --heading:#0a6cc4;
  --col-1:#1ea0f0;
  --col-2:#0878d0;
  --col-3:#00416e;
  --feat-head:#d4d4d4;
  --row:#eceefb;
  --rule:#ffffff;
  --ink:#222;
  --tick:#2ab94a;
}
*{box-sizing:border-box;margin:0;padding:0}
html,body{width:1200px;height:589px;overflow:hidden}
body{background:var(--canvas);font-family:'Roboto',sans-serif;position:relative;color:var(--ink)}
.page{position:absolute;top:104px;width:554px;height:454px;background:#fff;overflow:hidden}
.page--alacarte{left:30px}
.page--unlimited{left:614px}

.site-header{position:absolute;left:0;top:0;width:100%;height:42px;background:var(--header)}
.account-tab{position:absolute;left:356px;top:0;width:82px;height:10px;background:#3b3d40;color:#ddd;font-size:4.3px;display:flex;border-radius:0 0 4px 4px}
.account-tab span{flex:1;display:flex;align-items:center;justify-content:center}
.account-tab .signup{background:var(--nav);border-radius:0 0 4px 0;color:#fff}
.brand{position:absolute;left:111px;top:14px;display:flex;align-items:center;gap:4px;color:var(--brand);font-weight:700;font-size:10px;letter-spacing:.3px}
.brand i{width:9px;height:9px;background:var(--brand);display:block}
.phone-icon{position:absolute;left:335px;top:20px;width:13px;height:13px;border-radius:50%;background:var(--nav)}
.phone-icon svg{display:block}
.contact-lines{position:absolute;left:357px;top:19px;border-left:1px solid #555;padding-left:4px;color:#fff;font-size:5.6px;line-height:8.5px}
.contact-lines b{font-weight:700}

.main-nav{position:absolute;left:0;top:42px;width:100%;height:15px;background:var(--nav)}
.main-nav span{position:absolute;top:0;line-height:15px;color:#fff;font-size:4.4px;transform:translateX(-50%)}

.steps{position:absolute;left:0;top:57px;width:100%;height:43px;background:linear-gradient(100deg,#b3b4d2 0%,#c4b8d4 35%,#dbb6c6 62%,#f0c2b4 82%,#f9cca0 100%)}
.steps span{position:absolute;top:15px;font-size:11px;font-weight:700;color:#fff}
.steps .dash{top:13px;letter-spacing:1.5px;font-weight:500;color:#fff}
.steps .last{color:#3a3a3a}

.program-tabs{position:absolute;left:167px;top:107px;display:flex;height:22px}
.program-tabs span{width:110px;display:flex;align-items:center;justify-content:center;font-size:9.4px;background:var(--tab-off);color:#222}
.program-tabs .on{background:var(--tab-on);color:#fff}

.plan-title{position:absolute;left:0;width:100%;top:138px;text-align:center;color:var(--heading);font-size:11.5px;font-weight:500}

.price-table{position:absolute;left:29px;top:158px;width:496px;border:.6px solid #333;border-collapse:collapse;table-layout:fixed}
.price-table th{height:43px;color:#fff;font-weight:400;vertical-align:middle;text-align:center;padding-top:2px}
.price-table th.feat{width:170px;background:var(--feat-head);color:#222;font-size:14px;font-weight:700;letter-spacing:1.8px;border-right:.6px solid #333}
.price-table th.p1{background:var(--col-1)}
.price-table th.p2{background:var(--col-2)}
.price-table th.p3{background:var(--col-3)}
.amount{font-size:17px;text-decoration:underline;text-decoration-thickness:.8px;text-underline-offset:1.5px;line-height:17px}
.amount small{font-size:6px;text-decoration:none;display:inline-block;margin-left:1px}
.terms{font-size:6px;line-height:9px}
.price-table td{height:14.7px;background:var(--row);border-top:.6px solid var(--rule);font-size:8px;letter-spacing:.75px;text-align:center}
.price-table td.name{text-align:left;padding-left:9px}
.price-table td svg{width:7.5px;height:7.5px;display:block;margin:0 auto}
</style>
</head>
<body>
<svg width="0" height="0" style="position:absolute">
  <defs>
    <symbol id="tick" viewBox="0 0 16 16"><circle cx="8" cy="8" r="8" fill="#2ab94a"/><path d="M4.3 8.3l2.5 2.5 4.9-5" fill="none" stroke="#fff" stroke-width="2" stroke-linecap="round" stroke-linejoin="round"/></symbol>
    <symbol id="phone" viewBox="0 0 16 16"><path d="M5.2 4.2l1.4 1.6-.8 1.2c.6 1.3 1.6 2.3 2.9 2.9l1.2-.8 1.6 1.4-.8 1.3c-3.3-.3-6.1-3.1-6.4-6.4z" fill="#fff"/></symbol>
  </defs>
</svg>

<!-- À la carte -->
<section class="page page--alacarte">
  <header class="site-header">
    <div class="account-tab"><span>LOGIN</span><span class="signup">SIGN UP</span></div>
    <div class="brand"><i></i>BRIGHTLOOM REWARDS</div>
    <div class="phone-icon"><svg width="13" height="13"><use href="#phone"/></svg></div>
    <div class="contact-lines">USA Office : <b>619-555-0148</b><br>International : <b>1-800-555-0162</b></div>
  </header>
  <nav class="main-nav"><span style="left:133px">HOME</span><span style="left:180px">OUR INCENTIVES</span><span style="left:229px">SAMPLES</span><span style="left:272px">AFFILIATES</span><span style="left:321px">TESTIMONIALS</span><span style="left:362px">FAQ</span><span style="left:398px">CONTACT</span></nav>
  <div class="steps"><span style="left:46px">SIGN UP</span><span class="dash" style="left:100px">--------------------</span><span style="left:215px">SELECT PROGRAM</span><span class="dash" style="left:324px">--------------------</span><span class="last" style="left:442px">PAYMENT</span></div>
  <div class="program-tabs"><span class="on">AL A CARTE PROGRAM</span><span>UNLIMITED PROGRAM</span></div>
  <h2 class="plan-title">1 CERTIFICATE TYPE EACH MONTH</h2>
  <table class="price-table">
    <tr><th class="feat">FEATURES</th>
      <th class="p1"><div class="amount">$49/<small>MONTH</small></div><div class="terms">Month to Month<br>Basis No Contracts</div></th>
      <th class="p2"><div class="amount">$239</div><div class="terms">One Time Payment For<br>6 Months of Service</div></th>
      <th class="p3"><div class="amount">$399</div><div class="terms">One Time Payment For<br>12 Months of Service</div></th></tr>
    <tr><td class="name">Unlimited Certificate PDF Downloads</td><td><svg><use href="#tick"/></svg></td><td><svg><use href="#tick"/></svg></td><td><svg><use href="#tick"/></svg></td></tr>
    <tr><td class="name">Unlimited E-Mail Certificates</td><td><svg><use href="#tick"/></svg></td><td><svg><use href="#tick"/></svg></td><td><svg><use href="#tick"/></svg></td></tr>
    <tr><td class="name">Unlimited Text/SMS Certificates</td><td><svg><use href="#tick"/></svg></td><td><svg><use href="#tick"/></svg></td><td><svg><use href="#tick"/></svg></td></tr>
    <tr><td class="name">Unlimited API Usage</td><td><svg><use href="#tick"/></svg></td><td><svg><use href="#tick"/></svg></td><td><svg><use href="#tick"/></svg></td></tr>
    <tr><td class="name">Unlimited Web Banner Certificates</td><td><svg><use href="#tick"/></svg></td><td><svg><use href="#tick"/></svg></td><td><svg><use href="#tick"/></svg></td></tr>
    <tr><td class="name">Full Redemption Tracking</td><td><svg><use href="#tick"/></svg></td><td><svg><use href="#tick"/></svg></td><td><svg><use href="#tick"/></svg></td></tr>
    <tr><td class="name">Certificate Distribution Reports</td><td><svg><use href="#tick"/></svg></td><td><svg><use href="#tick"/></svg></td><td><svg><use href="#tick"/></svg></td></tr>
    <tr><td class="name">White Label Redemption Site</td><td><svg><use href="#tick"/></svg></td><td><svg><use href="#tick"/></svg></td><td><svg><use href="#tick"/></svg></td></tr>
    <tr><td class="name">End User Marketing Videos</td><td><svg><use href="#tick"/></svg></td><td><svg><use href="#tick"/></svg></td><td><svg><use href="#tick"/></svg></td></tr>
    <tr><td class="name">Marketing Posters and Flyers</td><td><svg><use href="#tick"/></svg></td><td><svg><use href="#tick"/></svg></td><td><svg><use href="#tick"/></svg></td></tr>
    <tr><td class="name">Product Description Brochures</td><td><svg><use href="#tick"/></svg></td><td><svg><use href="#tick"/></svg></td><td><svg><use href="#tick"/></svg></td></tr>
    <tr><td class="name">The Latest Tips</td><td><svg><use href="#tick"/></svg></td><td><svg><use href="#tick"/></svg></td><td><svg><use href="#tick"/></svg></td></tr>
    <tr><td class="name">Seperate Redemption Websites</td><td><svg><use href="#tick"/></svg></td><td><svg><use href="#tick"/></svg></td><td><svg><use href="#tick"/></svg></td></tr>
    <tr><td class="name">Contact Us 24/7</td><td><svg><use href="#tick"/></svg></td><td><svg><use href="#tick"/></svg></td><td><svg><use href="#tick"/></svg></td></tr>
    <tr><td class="name">Affiliate Program</td><td><svg><use href="#tick"/></svg></td><td><svg><use href="#tick"/></svg></td><td><svg><use href="#tick"/></svg></td></tr>
    <tr><td class="name">Discount Travel Booking Engine</td><td><svg><use href="#tick"/></svg></td><td><svg><use href="#tick"/></svg></td><td><svg><use href="#tick"/></svg></td></tr>
  </table>
</section>

<!-- Unlimited -->
<section class="page page--unlimited">
  <header class="site-header">
    <div class="account-tab"><span>LOGIN</span><span class="signup">SIGN UP</span></div>
    <div class="brand"><i></i>BRIGHTLOOM REWARDS</div>
    <div class="phone-icon"><svg width="13" height="13"><use href="#phone"/></svg></div>
    <div class="contact-lines">USA Office : <b>619-555-0148</b><br>International : <b>1-800-555-0162</b></div>
  </header>
  <nav class="main-nav"><span style="left:133px">HOME</span><span style="left:180px">OUR INCENTIVES</span><span style="left:229px">SAMPLES</span><span style="left:272px">AFFILIATES</span><span style="left:321px">TESTIMONIALS</span><span style="left:362px">FAQ</span><span style="left:398px">CONTACT</span></nav>
  <div class="steps"><span style="left:46px">SIGN UP</span><span class="dash" style="left:100px">--------------------</span><span style="left:215px">SELECT PROGRAM</span><span class="dash" style="left:324px">--------------------</span><span class="last" style="left:442px">PAYMENT</span></div>
  <div class="program-tabs"><span>AL A CARTE PROGRAM</span><span class="on">UNLIMITED PROGRAM</span></div>
  <h2 class="plan-title">1 CERTIFICATE TYPE EACH MONTH</h2>
  <table class="price-table">
    <tr><th class="feat">FEATURES</th>
      <th class="p1"><div class="amount">$99/<small>MONTH</small></div><div class="terms">Month to Month<br>Basis No Contracts</div></th>
      <th class="p2"><div class="amount">$495</div><div class="terms">One Time Payment For<br>6 Months of Service</div></th>
      <th class="p3"><div class="amount">$2,295</div><div class="terms">One Time Payment For<br>12 Months of Service</div></th></tr>
    <tr><td class="name">Unlimited Certificate PDF Downloads</td><td><svg><use href="#tick"/></svg></td><td><svg><use href="#tick"/></svg></td><td><svg><use href="#tick"/></svg></td></tr>
    <tr><td class="name">Unlimited E-Mail Certificates</td><td><svg><use href="#tick"/></svg></td><td><svg><use href="#tick"/></svg></td><td><svg><use href="#tick"/></svg></td></tr>
    <tr><td class="name">Unlimited Text/SMS Certificates</td><td><svg><use href="#tick"/></svg></td><td><svg><use href="#tick"/></svg></td><td><svg><use href="#tick"/></svg></td></tr>
    <tr><td class="name">Unlimited API Usage</td><td><svg><use href="#tick"/></svg></td><td><svg><use href="#tick"/></svg></td><td><svg><use href="#tick"/></svg></td></tr>
    <tr><td class="name">Unlimited Web Banner Certificates</td><td><svg><use href="#tick"/></svg></td><td><svg><use href="#tick"/></svg></td><td><svg><use href="#tick"/></svg></td></tr>
    <tr><td class="name">Full Redemption Tracking</td><td><svg><use href="#tick"/></svg></td><td><svg><use href="#tick"/></svg></td><td><svg><use href="#tick"/></svg></td></tr>
    <tr><td class="name">Certificate Distribution Reports</td><td><svg><use href="#tick"/></svg></td><td><svg><use href="#tick"/></svg></td><td><svg><use href="#tick"/></svg></td></tr>
    <tr><td class="name">White Label Redemption Site</td><td><svg><use href="#tick"/></svg></td><td><svg><use href="#tick"/></svg></td><td><svg><use href="#tick"/></svg></td></tr>
    <tr><td class="name">End User Marketing Videos</td><td><svg><use href="#tick"/></svg></td><td><svg><use href="#tick"/></svg></td><td><svg><use href="#tick"/></svg></td></tr>
    <tr><td class="name">Marketing Posters and Flyers</td><td><svg><use href="#tick"/></svg></td><td><svg><use href="#tick"/></svg></td><td><svg><use href="#tick"/></svg></td></tr>
    <tr><td class="name">Product Description Brochures</td><td><svg><use href="#tick"/></svg></td><td><svg><use href="#tick"/></svg></td><td><svg><use href="#tick"/></svg></td></tr>
    <tr><td class="name">The Latest Tips</td><td><svg><use href="#tick"/></svg></td><td><svg><use href="#tick"/></svg></td><td><svg><use href="#tick"/></svg></td></tr>
    <tr><td class="name">Seperate Redemption Websites</td><td><svg><use href="#tick"/></svg></td><td><svg><use href="#tick"/></svg></td><td><svg><use href="#tick"/></svg></td></tr>
    <tr><td class="name">Contact Us 24/7</td><td><svg><use href="#tick"/></svg></td><td><svg><use href="#tick"/></svg></td><td><svg><use href="#tick"/></svg></td></tr>
    <tr><td class="name">Affiliate Program</td><td><svg><use href="#tick"/></svg></td><td><svg><use href="#tick"/></svg></td><td><svg><use href="#tick"/></svg></td></tr>
    <tr><td class="name">Discount Travel Booking Engine</td><td><svg><use href="#tick"/></svg></td><td><svg><use href="#tick"/></svg></td><td><svg><use href="#tick"/></svg></td></tr>
  </table>
</section>
</body>
</html>
```